Need Business Card for our Real Estate Business with Sales Executive's Picture

PANTONE 484 C ( RED)

PANTONE 2766 C ( BLUE

Industry/Entity Type

Real Estate

Contact Information for Business Card

Name, Mobile, email, & picture of Person
Agency Phone, address, Web address

Requirements
Must have
• Our Logo Colours, Agent Picture,

```html
<!DOCTYPE html>
<html lang="en">
<head>
<meta charset="utf-8">
<title>Kestrel Business Card – Front and Back</title>
<link rel="stylesheet" href="https://fonts.googleapis.com/css2?family=Cabin:wght@400;500;700&family=Montserrat:wght@800&display=swap">
<style>
  :root {
    --navy: #0b1438;
    --maroon: #6b0d10;
    --paper: #ffffff;
    --soft-text: #dfe2ec;
    --guide: #8a8a8a;
    --photo-light: #e9eae6;
    --photo-mid: #c9ccd0;
    --photo-suit: #2c3f86;
  }
  * { box-sizing: border-box; margin: 0; padding: 0; }
  html, body { width: 990px; height: 1200px; overflow: hidden; background: var(--paper); }
  body { position: relative; font-family: "Cabin", sans-serif; }

  .side-label {
    position: absolute; left: 0; width: 970px; text-align: center;
    font-family: "Montserrat", sans-serif; font-weight: 800; font-size: 32px;
    letter-spacing: 1.5px; color: #000;
  }
  .side-label--front { top: 18px; }
  .side-label--back { top: 1118px; }

  .card { position: absolute; overflow: hidden; }
  .card--front { left: 58px; top: 70px; width: 851px; height: 496px; background: var(--navy); }
  .card--back { left: 63px; top: 613px; width: 850px; height: 494px; background: var(--navy); }

  .agent-photo {
    position: absolute; left: 0; top: 0; width: 372px; height: 496px;
    background:
      radial-gradient(ellipse 150px 260px at 200px 330px, var(--photo-suit) 0%, rgba(44,63,134,0.85) 55%, rgba(44,63,134,0) 100%),
      linear-gradient(135deg, var(--photo-light) 0%, var(--photo-mid) 100%);
  }
  .accent-bar { position: absolute; left: 372px; top: 0; width: 13px; height: 496px; background: var(--maroon); }

  .name-plate {
    position: absolute; left: 0; top: 363px; width: 447px; height: 100px;
    background: rgba(232, 234, 240, 0.62); border-radius: 0 24px 24px 0;
  }
  .agent-name {
    position: absolute; left: 44px; top: 372px;
    font-weight: 700; font-size: 40px; color: var(--navy); letter-spacing: 0.5px;
  }
  .agent-title {
    position: absolute; left: 44px; top: 417px;
    font-weight: 400; font-size: 26px; color: var(--navy);
  }

  .guide { position: absolute; border: 2px dashed var(--guide); pointer-events: none; }
  .card--front .guide { left: 29px; top: 30px; width: 794px; height: 438px; }
  .card--back .guide { left: 25px; top: 29px; width: 793px; height: 437px; }

  .wordmark {
    position: absolute; display: flex; align-items: center; justify-content: center; gap: 14px;
    font-family: "Cabin", sans-serif; font-weight: 500; color: var(--paper); letter-spacing: 6px;
  }
  .wordmark__square { background: var(--maroon); flex: none; }
  .card--front .wordmark { left: 385px; width: 466px; top: 138px; font-size: 50px; }
  .card--front .wordmark__square { width: 14px; height: 14px; }
  .card--back .wordmark { left: 0; width: 850px; top: 248px; font-size: 84px; letter-spacing: 10px; }
  .card--back .wordmark__square { width: 22px; height: 22px; }

  .contact { position: absolute; color: var(--soft-text); font-size: 19px; letter-spacing: 0.6px; display: flex; align-items: center; gap: 8px; white-space: nowrap; }
  .contact svg { flex: none; fill: var(--soft-text); }
  .contact--address { left: 533px; top: 271px; }
  .contact--phone { left: 423px; top: 324px; }
  .contact--fax { left: 628px; top: 322px; }
  .contact--email { left: 533px; top: 367px; }
  .contact--social { left: 567px; top: 429px; font-size: 15px; }
  .social-square { width: 17px; height: 17px; background: #3b5a9a; border-radius: 2px; }

  .website { position: absolute; left: 0; width: 850px; top: 378px; text-align: center; color: var(--soft-text); font-size: 23px; letter-spacing: 1px; }
</style>
</head>
<body>
  <div class="side-label side-label--front">FRONT</div>

  <section class="card card--front">
    <div class="agent-photo" role="img" aria-label="Portrait photo of the sales executive in a navy suit"></div>
    <div class="accent-bar"></div>
    <div class="name-plate"></div>
    <div class="agent-name">FULL NAME</div>
    <div class="agent-title">Job Title</div>

    <div class="wordmark"><span class="wordmark__square"></span>KESTREL</div>

    <div class="contact contact--address">Address Line 1</div>
    <div class="contact contact--phone">
      <svg width="22" height="22" viewBox="0 0 24 24"><path d="M6.6 10.8a15.1 15.1 0 0 0 6.6 6.6l2.2-2.2a1 1 0 0 1 1-.25 11.4 11.4 0 0 0 3.6.57 1 1 0 0 1 1 1V20a1 1 0 0 1-1 1A17 17 0 0 1 3 4a1 1 0 0 1 1-1h3.5a1 1 0 0 1 1 1c0 1.25.2 2.45.57 3.6a1 1 0 0 1-.25 1z"/></svg>
      Phone / Other
    </div>
    <div class="contact contact--fax">
      <svg width="24" height="22" viewBox="0 0 24 22"><rect x="0" y="5" width="6" height="16" rx="1"/><rect x="8" y="0" width="12" height="8"/><rect x="7" y="9" width="17" height="12" rx="1"/><rect x="10" y="12" width="3" height="2" fill="#0b1438"/><rect x="15" y="12" width="3" height="2" fill="#0b1438"/><rect x="10" y="16" width="3" height="2" fill="#0b1438"/><rect x="15" y="16" width="3" height="2" fill="#0b1438"/></svg>
      Fax / Other
    </div>
    <div class="contact contact--email">
      <svg width="24" height="17" viewBox="0 0 24 17"><path d="M1 1h22v15H1z" fill="none" stroke="#dfe2ec" stroke-width="2"/><path d="M1 1l11 9 11-9" fill="none" stroke="#dfe2ec" stroke-width="2"/></svg>
      Email / Other
    </div>
    <div class="contact contact--social"><span class="social-square"></span>@Name</div>

    <div class="guide"></div>
  </section>

  <section class="card card--back">
    <div class="wordmark"><span class="wordmark__square"></span>KESTREL</div>
    <div class="website">www.kestrelhomes.com</div>
    <div class="guide"></div>
  </section>

  <div class="side-label side-label--back">BACK</div>
</body>
</html>
```